Home Builder and Trade Supplier needs a Ad/leaflet/mail drop off leaflet design

HavenCrest is a business that builds homes, renovations, property maintenance and anything else construction related to residential homes. See photos I have attached that have a description of the business.

I'm after a double sided flyer for mail box drop offs. The market audience is up market expensive homes and offices. I have attached some examples of what i think would look good - I would like to see an example like or similar to that but by all means the designs you submit don't have to be a copy or similar. If you have something completely different in mind that you think would suit, please submit or even a rough draft if youre not sure I'll like it and you don't want to risk wasting time.

Please include the text and information in your designs that I have included in my examples.

Submissions before the 10 days are welcome and encouraged :)

Any questions, please feel free to ask on here or through email on: joram.k@mailvista.net

Pamphlet Size: 210 x 142mm (a quarter of an A4)
Double Sided Colour

Property Maintenance

Requirements
Must have
• Contact Us: 0412 958 601
www.havencresthomes.com.au
Double sided
Colour
Size: quater of an A4

```html
<!DOCTYPE html>
<html lang="en">
<head>
<meta charset="utf-8">
<title>HavenCrest Flyer</title>
<link rel="stylesheet" href="https://fonts.googleapis.com/css2?family=Oswald:wght@400;500;600&family=Open+Sans:wght@300;400&display=swap">
<style>
  :root {
    --bg: #e9e6e2;
    --white: #ffffff;
    --orange: #e8835a;
    --orange-dark: #d9683e;
    --black: #0d0d0d;
    --ink: #1a1a1a;
    --light: #fdf3ee;
    --grey: #d8d8d8;
  }
  * { box-sizing: border-box; margin: 0; padding: 0; }
  html, body { width: 1200px; height: 438px; overflow: hidden; background: var(--bg); }
  .flyer {
    position: absolute; top: 33px; width: 555px; height: 372px;
    background: var(--white); overflow: hidden;
    box-shadow: 0 4px 14px rgba(0,0,0,.25);
  }
  .flyer--front { left: 35px; }
  .flyer--back { left: 617px; }
  .wave { position: absolute; left: 0; top: 0; width: 555px; height: 372px; }
  .photo { position: absolute; }
  .photo--lamps { left: 90px; top: 0; width: 465px; height: 160px;
    background: linear-gradient(90deg, #f2f2f2 0%, #c93a32 35%, #f0f0f0 55%, #2e3038 80%, #f2f2f2 100%); opacity: .85; }
  .photo--round { border-radius: 50%; border: 4px solid var(--white); box-shadow: 0 2px 6px rgba(0,0,0,.35); }
  .photo--digger { left: 2px; top: 262px; width: 100px; height: 100px; background: radial-gradient(circle, #f0c23a, #6a6a6a 70%, #eee); }
  .photo--cable { left: 80px; top: 250px; width: 112px; height: 112px; background: radial-gradient(circle, #c88050, #c92a2a 60%, #e7e7e7); }
  .photo--paint { left: 180px; top: 262px; width: 100px; height: 100px; background: radial-gradient(circle, #2a6acb, #d9c89a 65%, #f0f0f0); }
  .photo--toolbelt { left: 38px; top: 18px; width: 172px; height: 172px; background: radial-gradient(circle, #e2b440, #7a5530 65%, #f4f4f4); }
  .photo--paintcan { left: 262px; top: 18px; width: 270px; height: 125px;
    background: linear-gradient(90deg, transparent 0%, #c9c9c9 20%, #d3332c 55%, #b9b9b9 80%, transparent 100%); opacity: .8; }
  .brand {
    position: absolute; left: 0; top: 57px; width: 170px; height: 56px;
    background: var(--black); display: flex; align-items: center; gap: 8px; padding-left: 10px;
  }
  .brand__mark { width: 26px; height: 26px; background: var(--white); }
  .brand__name { font-family: "Oswald", sans-serif; font-weight: 500; font-size: 24px; color: var(--white); letter-spacing: .5px; }
  .intro {
    position: absolute; left: 14px; top: 174px; width: 320px;
    font-family: "Oswald", sans-serif; font-weight: 400; font-size: 15.5px; line-height: 1.25;
    color: var(--white); text-transform: uppercase; text-align: center;
  }
  .intro strong { color: var(--ink); font-weight: 600; font-size: 20px; }
  .pitch {
    position: absolute; left: 353px; top: 197px; width: 180px;
    font-family: "Oswald", sans-serif; font-size: 8.5px; line-height: 1.3; color: var(--white); text-transform: uppercase;
  }
  .pitch p + p { margin-top: 9px; }
  .bar {
    position: absolute; left: 0; bottom: 0; width: 555px; height: 36px; background: var(--black);
    display: flex; align-items: center; color: var(--white);
  }
  .bar--front { justify-content: flex-end; padding-right: 28px; font-family: "Open Sans", sans-serif; font-size: 17px; }
  .bar--back { justify-content: center; gap: 12px; font-family: "Oswald", sans-serif; font-size: 19px; padding-left: 20px; }
  .phone { display: flex; align-items: center; gap: 8px; }
  .services-title {
    position: absolute; left: 0; width: 555px; top: 187px; text-align: center;
    font-family: "Oswald", sans-serif; font-weight: 500; font-size: 18px; color: var(--ink); text-transform: uppercase;
  }
  .services {
    position: absolute; left: 14px; top: 224px; width: 540px;
    display: grid; grid-template-columns: 108px 118px 116px 92px 100px; row-gap: 3px;
    list-style: none; font-family: "Open Sans", sans-serif; font-size: 13px; color: var(--light);
  }
  .services li::before { content: "\2192"; margin-right: 4px; }
</style>
</head>
<body>
  <section class="flyer flyer--front">
    <div class="photo photo--lamps" role="img" aria-label="Glossy red, white and black pendant lamps"></div>
    <svg class="wave" viewBox="0 0 555 372" aria-hidden="true">
      <path d="M0 165 C140 150 250 112 555 150 V372 H0Z" fill="var(--grey)"/>
      <path d="M0 172 C150 158 260 122 555 158 V372 H0Z" fill="var(--orange)"/>
    </svg>
    <div class="brand"><span class="brand__mark"></span><span class="brand__name">HavenCrest</span></div>
    <p class="intro"><strong>HavenCrest is</strong> one of the preffered home builders and residential trade supplier for customer across Sydeny.</p>
    <div class="pitch">
      <p>A one stop shop.we can build your entire home or supply you with our specialist tradesman.</p>
      <p>No matter how small or large your job is,contact us to find out how we can help you</p>
    </div>
    <div class="bar bar--front">www.havencresthomes.com.au</div>
    <div class="photo photo--round photo--digger" role="img" aria-label="Excavator arm"></div>
    <div class="photo photo--round photo--paint" role="img" aria-label="Open tin of blue paint"></div>
    <div class="photo photo--round photo--cable" role="img" aria-label="Copper electrical cables"></div>
  </section>

  <section class="flyer flyer--back">
    <div class="photo photo--paintcan" role="img" aria-label="Paint brush and can with red paint"></div>
    <svg class="wave" viewBox="0 0 555 372" aria-hidden="true">
      <path d="M0 150 C150 130 300 105 555 140 V372 H0Z" fill="var(--grey)"/>
      <path d="M0 157 C150 138 300 113 555 148 V372 H0Z" fill="var(--orange)"/>
    </svg>
    <div class="photo photo--round photo--toolbelt" role="img" aria-label="Leather tool belt with tools"></div>
    <h2 class="services-title">Contact us for:</h2>
    <ul class="services">
      <li>New Homes</li><li>Maintenance</li><li>Painting</li><li>Tiling</li><li>Demoliation</li>
      <li>Renovations</li><li>Strata</li><li>Electrical</li><li>Glazing</li><li>Excavation</li>
      <li>Architecture</li><li>Air Condition</li><li>Lawn Mowing</li><li>Bricklaying</li><li>Carpentry</li>
      <li>Engineering</li><li>Plumbing</li><li>Landscaping</li><li>Roofing</li><li>Cleaning</li>
    </ul>
    <div class="bar bar--back">
      <span>WWW.HAVENCRESTHOMES.COM.AU</span>
      <span class="phone">
        <svg width="20" height="20" viewBox="0 0 20 20" aria-hidden="true">
          <rect x="0" y="0" width="20" height="20" rx="3" fill="var(--white)"/>
          <path d="M6 4 L8.5 4 L9.5 7 L8 8.2 C8.8 10 10 11.2 11.8 12 L13 10.5 L16 11.5 V14 C16 15 15 16 14 16 C8.5 15.5 4.5 11.5 4 6 C4 5 5 4 6 4Z" fill="var(--black)"/>
        </svg>
        0412 958 601
      </span>
    </div>
  </section>
</body>
</html>
```